Create a business promotion flyer to leave in customer mailboxes. We are a bulk petroleum supplier, servicing any industry that requires diesel. Base in griffith NSW, servicing griffith area and surrounds.

Business Name - Terra Diesel
Fuel@terradiesel-example.com.au
Marco - 0412 309 768 mpellucci@terradiesel-example.com.au
Liam - 0431 672 095 lhartwell@terradiesel-example.com.au
Simon - 0465 218 347 sbrack@terradiesel-example.com.au
Office 02 6931 7852

Bulk Fuel deliveries.
Oils & lubricants
Local Family owned business

```html
<!DOCTYPE html>
<html lang="en">
<head>
<meta charset="utf-8">
<title>Terra Diesel – Bulk Fuel Flyer</title>
<link href="https://fonts.googleapis.com/css2?family=Outfit:wght@700;800&family=Inter:wght@400;500;700&display=swap" rel="stylesheet">
<style>
:root{
  --red:#e8261c;
  --ink:#555657;
  --text:#2b2b2b;
  --backdrop:#a3a4a8;
  --panel:#6c6c6c;
  --pill:#8e8e8e;
  --tile:#f3f3f3;
  --white:#ffffff;
}
*{margin:0;padding:0;box-sizing:border-box}
html,body{width:1200px;height:830px;overflow:hidden}
body{background:var(--backdrop);font-family:"Inter",sans-serif;color:var(--text);position:relative}
.page{position:absolute;width:482px;height:682px;background:var(--white);overflow:hidden}
.page--front{left:82px;top:75px}
.page--back{left:634px;top:74px}
.abs{position:absolute}
.heading{font-family:"Outfit",sans-serif;font-weight:800;color:var(--ink);line-height:1.05;text-transform:uppercase;letter-spacing:-0.1px;white-space:nowrap}
.heading .accent{color:var(--red)}
.body-copy{font-size:10px;line-height:14px;color:var(--text)}

/* front header */
.brand{left:19px;top:32px;display:flex;align-items:center;gap:6px;font-family:"Outfit",sans-serif;font-weight:700;font-size:17px;color:var(--red);white-space:nowrap}
.brand__mark{width:11px;height:11px;background:var(--red)}
.header-rule{left:140px;top:19px;width:1.5px;height:46px;background:var(--ink)}
.headline{left:162px;top:19px;font-size:19.5px;line-height:25px;letter-spacing:-0.2px}

.photo{background:linear-gradient(180deg,#ffffff 0%,#a9c4e4 14%,#c9d8ea 40%,#9aa0a8 62%,#d8d8d8 100%)}
.photo--hero{left:0;top:76px;width:482px;height:230px}
.swoosh{left:0;top:236px}

.why-title{left:15px;top:320px;font-size:15px}
.feature{background:var(--tile);border-radius:4px;display:flex;flex-direction:column;align-items:center;justify-content:center;gap:4px;font-size:9.5px;line-height:12px;text-align:center;color:var(--text)}
.feature--wide{flex-direction:row;gap:14px;text-align:left}
.feature svg{stroke:var(--red);fill:none;stroke-width:1.6;stroke-linecap:round;stroke-linejoin:round}

.trusted{left:248px;top:294px;font-size:14.5px}
.trusted-copy{left:248px;top:336px;width:222px}
.supply-title{left:248px;top:427px;font-size:14.5px}
.supply-list{left:248px;top:452px;width:170px;list-style:none}
.supply-list li{height:19px;margin-bottom:3.7px;display:flex;align-items:center;gap:9px;padding-left:9px;font-size:9.5px;background:linear-gradient(90deg,#eeeeee 60%,rgba(238,238,238,0));width:170px}

/* contact footer */
.footer{left:0;top:548px;width:482px;height:134px}
.footer__band{position:absolute;left:0;top:0}
.pill{position:absolute;top:21px;height:37px;border-radius:19px;background:var(--pill);display:flex;align-items:center;gap:8px;padding-left:9px;color:var(--white);font-weight:500;white-space:nowrap}
.pill__icon{width:25px;height:25px;border-radius:50%;background:var(--white);display:flex;align-items:center;justify-content:center;flex:none}
.pill--phone{left:17px;width:216px;font-size:14.5px}
.pill--phone b{font-weight:700}
.pill--email{left:246px;width:222px;font-size:9.6px;font-weight:700}
.contact{position:absolute;top:72px;color:var(--white);white-space:nowrap}
.contact__name{font-family:"Outfit",sans-serif;font-weight:800;font-size:12.5px;line-height:13px}
.contact__phone{font-family:"Outfit",sans-serif;font-weight:800;font-size:15px;line-height:16px}
.contact__email{font-size:7.3px;margin-top:5px;letter-spacing:-0.1px}
.contact-rule{position:absolute;top:72px;width:1px;height:48px;background:rgba(255,255,255,.8)}

/* back page */
.back-headline{left:20px;top:24px;font-size:16.5px}
.back-intro{left:20px;top:51px;width:440px}
.industries{left:18px;top:108px;width:443px;height:199px;background:var(--panel);border-radius:12px}
.industries__title{position:absolute;left:18px;top:13px;font-family:"Outfit",sans-serif;font-weight:800;font-size:11.5px;color:var(--white)}
.industry{position:absolute;width:98px;height:66px;border:1px solid rgba(255,255,255,.55);border-radius:10px;display:flex;flex-direction:column;align-items:center;justify-content:center;gap:4px;color:var(--white);font-size:9.5px;line-height:11.5px;text-align:center}
.industry svg{stroke:var(--white);fill:none;stroke-width:1.4;stroke-linejoin:round;stroke-linecap:round}

.trust-title{left:20px;top:329px;font-size:16.5px;line-height:21px}
.trust-list{left:24px;top:381px;list-style:none}
.trust-list li{display:flex;align-items:center;gap:8px;height:18.3px;font-size:10px}
.more-card{left:248px;top:330px;width:214px;height:154px;background:var(--tile);border-radius:8px;overflow:hidden}
.more-card__title{position:absolute;left:15px;top:12px;font-size:14px}
.more-card__copy{position:absolute;left:16px;top:32px;width:190px;font-size:7.8px;line-height:10px}
.photo--card{position:absolute;left:0;top:66px;width:214px;height:88px;background:linear-gradient(180deg,#f3f3f3 0%,#a9c4e4 20%,#c9d8ea 45%,#9aa0a8 70%,#d8d8d8 100%)}
.cta{left:0;top:510px;width:482px;text-align:center;font-size:16.5px}
.cta-copy{left:0;top:535px;width:482px;text-align:center;font-size:10px}
</style>
</head>
<body>

<!-- FRONT -->
<section class="page page--front">
  <div class="abs brand"><span class="brand__mark"></span>Terra Diesel</div>
  <div class="abs header-rule"></div>
  <h1 class="abs heading headline">Reliable bulk fuel supply<br>for <span class="accent">local businesses</span></h1>

  <div class="abs photo photo--hero" role="img" aria-label="Photo of a white Terra Diesel road-train fuel tanker parked in front of a large steel depot shed under a blue sky"></div>
  <svg class="abs swoosh" width="482" height="72" viewBox="0 0 482 72" aria-hidden="true">
    <path d="M0 72 C120 30 300 18 482 20 L482 72 Z" fill="#fff"/>
    <path d="M0 66 C120 24 300 12 482 14 L482 26 C300 22 140 32 0 72 Z" fill="#e8261c"/>
  </svg>

  <h2 class="abs heading why-title">Why choose <span class="accent">Terra Diesel?</span></h2>
  <div class="abs feature" style="left:14px;top:353px;width:120px;height:64px">
    <svg width="20" height="20" viewBox="0 0 20 20"><path d="M10 1.5 17 4v6c0 4-3 7-7 8.5C6 17 3 14 3 10V4z"/><circle cx="7.5" cy="8.5" r="1.6"/><circle cx="12.5" cy="8.5" r="1.6"/><path d="M5 13c.5-1.5 1.5-2 2.5-2s2 .5 2.5 2m0 0c.5-1.5 1.5-2 2.5-2s2 .5 2.5 2"/></svg>
    <span>Local Family-Owned<br>Business</span>
  </div>
  <div class="abs feature" style="left:141px;top:353px;width:83px;height:64px">
    <svg width="20" height="20" viewBox="0 0 20 20"><circle cx="11" cy="6" r="4.5"/><path d="M11 3.5v5M12.5 4.5h-2.2a1 1 0 0 0 0 2h1.4a1 1 0 0 1 0 2H9.5"/><path d="M2 13h3l3 1.5h3.5a1 1 0 0 1 0 2H8M2 18h4l5 .5 6-3.5a1 1 0 0 0-1.5-1.5L12 15"/></svg>
    <span>Competitive<br>Pricing</span>
  </div>
  <div class="abs feature" style="left:14px;top:421px;width:120px;height:64px">
    <svg width="20" height="20" viewBox="0 0 20 20"><path d="M10 1.5 17 4v6c0 4-3 7-7 8.5C6 17 3 14 3 10V4z"/><path d="m7 10 2 2 4-4"/></svg>
    <span>Reliable &amp; Prompt<br>Deliveries</span>
  </div>
  <div class="abs feature" style="left:141px;top:421px;width:83px;height:64px">
    <svg width="20" height="20" viewBox="0 0 20 20"><circle cx="10" cy="7.5" r="4"/><path d="M4.5 8a5.5 5.5 0 0 1 11 0M4 7v3M16 7v3M16 10c0 1.5-1.5 2.5-4 2.5M3 19c0-4 3-6 7-6s7 2 7 6"/></svg>
    <span>Personal<br>Service</span>
  </div>
  <div class="abs feature feature--wide" style="left:14px;top:494px;width:209px;height:49px">
    <svg width="22" height="22" viewBox="0 0 22 22"><path d="M11 14s-4.5-4.2-4.5-7.5a4.5 4.5 0 0 1 9 0C15.5 9.8 11 14 11 14z"/><circle cx="11" cy="6.5" r="1.6"/><path d="M6 12 2 20h18l-4-8M6 17l5-2 5 3"/></svg>
    <span>Servicing Griffith &amp;<br>Surrounding Areas</span>
  </div>

  <h2 class="abs heading trusted">Your trusted local<br><span class="accent">diesel supplier</span></h2>
  <p class="abs body-copy trusted-copy">Whether you're in agriculture, transport, construction, earthmoving, mining, manufacturing, or any industry that relies on diesel, Terra Diesel delivers quality bulk fuel directly to your site—on time, every time.</p>

  <h2 class="abs heading supply-title">We <span class="accent">supply</span></h2>
  <ul class="abs supply-list">
    <li><svg width="9" height="7" viewBox="0 0 9 7"><path d="M1 3.5 3.3 6 8 1" stroke="#e8261c" stroke-width="1.6" fill="none"/></svg>Bulk Diesel Deliveries</li>
    <li><svg width="9" height="7" viewBox="0 0 9 7"><path d="M1 3.5 3.3 6 8 1" stroke="#e8261c" stroke-width="1.6" fill="none"/></svg>Premium Oils &amp; Lubricants</li>
    <li><svg width="9" height="7" viewBox="0 0 9 7"><path d="M1 3.5 3.3 6 8 1" stroke="#e8261c" stroke-width="1.6" fill="none"/></svg>Fast &amp; Reliable Local Service</li>
    <li><svg width="9" height="7" viewBox="0 0 9 7"><path d="M1 3.5 3.3 6 8 1" stroke="#e8261c" stroke-width="1.6" fill="none"/></svg>Flexible Delivery Solutions</li>
  </ul>

  <div class="abs footer">
    <svg class="footer__band" width="482" height="134" viewBox="0 0 482 134" aria-hidden="true"><path d="M0 0 L22 34 L482 34 L482 134 L0 134 Z" fill="#e8261c"/></svg>
    <div class="pill pill--phone"><span class="pill__icon"><svg width="13" height="13" viewBox="0 0 24 24"><path d="M6.6 10.8a15 15 0 0 0 6.6 6.6l2.2-2.2a1 1 0 0 1 1-.25 11.4 11.4 0 0 0 3.6.6 1 1 0 0 1 1 1V20a1 1 0 0 1-1 1A17 17 0 0 1 3 4a1 1 0 0 1 1-1h3.5a1 1 0 0 1 1 1c0 1.25.2 2.45.6 3.6a1 1 0 0 1-.25 1z" fill="#8e8e8e"/></svg></span>Office&nbsp;<b>02 6931 7852</b></div>
    <div class="pill pill--email"><span class="pill__icon"><svg width="14" height="11" viewBox="0 0 14 11"><rect x="1" y="1" width="12" height="9" rx="1" fill="none" stroke="#8e8e8e" stroke-width="1.3"/><path d="m1.5 1.8 5.5 4.2 5.5-4.2" fill="none" stroke="#8e8e8e" stroke-width="1.3"/></svg></span>Fuel@terradiesel-example.com.au</div>
    <div class="contact" style="left:19px"><div class="contact__name">MARCO</div><div class="contact__phone">0412 309 768</div><div class="contact__email">mpellucci@terradiesel-example.com.au</div></div>
    <div class="contact-rule" style="left:163px"></div>
    <div class="contact" style="left:189px"><div class="contact__name">LIAM</div><div class="contact__phone">0431 672 095</div><div class="contact__email">lhartwell@terradiesel-example.com.au</div></div>
    <div class="contact-rule" style="left:322px"></div>
    <div class="contact" style="left:349px"><div class="contact__name">SIMON</div><div class="contact__phone">0465 218 347</div><div class="contact__email">sbrack@terradiesel-example.com.au</div></div>
  </div>
</section>

<!-- BACK -->
<section class="page page--back">
  <h2 class="abs heading back-headline"><span class="accent">Fuel delivered</span> when you need it most</h2>
  <p class="abs body-copy back-intro">At Terra Diesel, we understand that downtime costs money. That's why we provide dependable bulk fuel deliveries to businesses throughout Griffith and surrounding regions, helping keep your equipment, vehicles, and operations running efficiently.</p>

  <div class="abs industries">
    <div class="industries__title">INDUSTRIES WE SERVICE</div>
    <div class="industry" style="left:13px;top:41px"><svg width="20" height="20" viewBox="0 0 20 20"><circle cx="10" cy="10" r="8.5"/><path d="M10 16V6M10 10c-2 0-3-1.5-3-3 2 0 3 1.5 3 3zm0 0c2 0 3-1.5 3-3-2 0-3 1.5-3 3zm0 3c-2 0-3-1.5-3-3 2 0 3 1.5 3 3zm0 0c2 0 3-1.5 3-3-2 0-3 1.5-3 3z"/></svg>Agriculture &amp;<br>Farming</div>
    <div class="industry" style="left:120px;top:41px"><svg width="24" height="20" viewBox="0 0 24 20"><path d="M2 15V5h13v10M15 8h4l3 4v3h-2M2 15h2M10 15h6"/><circle cx="7" cy="15.5" r="2"/><circle cx="18" cy="15.5" r="2"/></svg>Transport<br>&amp; Logistics</div>
    <div class="industry" style="left:227px;top:41px"><svg width="22" height="22" viewBox="0 0 22 22"><path d="M5 21V3h3v18M3 21h16M8 4h11M8 4l3-2M17 4v4M13 21v-7h6v7M15 17h2"/></svg>Construction</div>
    <div class="industry" style="left:332px;top:41px"><svg width="24" height="20" viewBox="0 0 24 20"><path d="M3 12V7h6l2 5M11 12h-8M12 9l5-6 4 5-2 3M19 11l2 3h-3"/><rect x="2" y="13" width="12" height="4" rx="2"/></svg>Earthmoving</div>
    <div class="industry" style="left:13px;top:118px"><svg width="20" height="22" viewBox="0 0 20 22"><path d="M5 8a5 5 0 0 1 10 0M4 8h12M7 9a3 3 0 0 0 6 0M3 21v-4c0-2 2-4 7-4s7 2 7 4v4M10 13v8M7 13l3 3 3-3"/></svg>Civil Contractors</div>
    <div class="industry" style="left:120px;top:118px"><svg width="22" height="22" viewBox="0 0 22 22"><circle cx="11" cy="11" r="3"/><circle cx="11" cy="11" r="6.5"/><path d="M11 2v2M11 18v2M2 11h2M18 11h2M4.6 4.6 6 6M16 16l1.4 1.4M4.6 17.4 6 16M16 6l1.4-1.4"/></svg>Manufacturing</div>
    <div class="industry" style="left:227px;top:118px"><svg width="24" height="20" viewBox="0 0 24 20"><path d="M3 9h18l-2 7H5zM6 9l2-4 3 2 3-3 3 2 2 3"/><circle cx="8" cy="17.5" r="1.5"/><circle cx="16" cy="17.5" r="1.5"/></svg>Mining</div>
    <div class="industry" style="left:332px;top:118px"><svg width="24" height="20" viewBox="0 0 24 20"><path d="M2 12V3h9v9M11 6h3l2 3v3M8 14v-3h9v6M17 13h3l2 3v2"/><circle cx="12" cy="18" r="1.5"/><circle cx="19" cy="18" r="1.5"/></svg>Fleet Operators</div>
  </div>

  <h2 class="abs heading trust-title"><span class="accent">Why local businesses</span><br>trust Terra Diesel</h2>
  <ul class="abs trust-list">
    <li><svg width="9" height="7" viewBox="0 0 9 7"><path d="M1 3.5 3.3 6 8 1" stroke="#e8261c" stroke-width="1.6" fill="none"/></svg>Fast Local Delivery</li>
    <li><svg width="9" height="7" viewBox="0 0 9 7"><path d="M1 3.5 3.3 6 8 1" stroke="#e8261c" stroke-width="1.6" fill="none"/></svg>Reliable Customer Service</li>
    <li><svg width="9" height="7" viewBox="0 0 9 7"><path d="M1 3.5 3.3 6 8 1" stroke="#e8261c" stroke-width="1.6" fill="none"/></svg>Quality Fuel Products</li>
    <li><svg width="9" height="7" viewBox="0 0 9 7"><path d="M1 3.5 3.3 6 8 1" stroke="#e8261c" stroke-width="1.6" fill="none"/></svg>Family-Owned &amp; Operated</li>
    <li><svg width="9" height="7" viewBox="0 0 9 7"><path d="M1 3.5 3.3 6 8 1" stroke="#e8261c" stroke-width="1.6" fill="none"/></svg>Experienced Local Team</li>
    <li><svg width="9" height="7" viewBox="0 0 9 7"><path d="M1 3.5 3.3 6 8 1" stroke="#e8261c" stroke-width="1.6" fill="none"/></svg>Flexible Supply Solutions</li>
  </ul>

  <div class="abs more-card">
    <h3 class="heading more-card__title"><span class="accent">More than</span> just fuel</h3>
    <p class="more-card__copy">We also supply a quality range of oils and lubricants to help protect your machinery and maximise performance.</p>
    <div class="photo--card" role="img" aria-label="Photo of the Terra Diesel fuel tanker road train at the depot"></div>
  </div>

  <h2 class="abs heading cta">Let's keep your <span class="accent">business moving</span></h2>
  <p class="abs body-copy cta-copy">For competitive pricing and dependable fuel supply, contact the Terra Diesel team today.</p>

  <div class="abs footer">
    <svg class="footer__band" width="482" height="134" viewBox="0 0 482 134" aria-hidden="true"><path d="M0 0 L22 34 L482 34 L482 134 L0 134 Z" fill="#e8261c"/></svg>
    <div class="pill pill--phone"><span class="pill__icon"><svg width="13" height="13" viewBox="0 0 24 24"><path d="M6.6 10.8a15 15 0 0 0 6.6 6.6l2.2-2.2a1 1 0 0 1 1-.25 11.4 11.4 0 0 0 3.6.6 1 1 0 0 1 1 1V20a1 1 0 0 1-1 1A17 17 0 0 1 3 4a1 1 0 0 1 1-1h3.5a1 1 0 0 1 1 1c0 1.25.2 2.45.6 3.6a1 1 0 0 1-.25 1z" fill="#8e8e8e"/></svg></span>Office&nbsp;<b>02 6931 7852</b></div>
    <div class="pill pill--email"><span class="pill__icon"><svg width="14" height="11" viewBox="0 0 14 11"><rect x="1" y="1" width="12" height="9" rx="1" fill="none" stroke="#8e8e8e" stroke-width="1.3"/><path d="m1.5 1.8 5.5 4.2 5.5-4.2" fill="none" stroke="#8e8e8e" stroke-width="1.3"/></svg></span>Fuel@terradiesel-example.com.au</div>
    <div class="contact" style="left:19px"><div class="contact__name">MARCO</div><div class="contact__phone">0412 309 768</div><div class="contact__email">mpellucci@terradiesel-example.com.au</div></div>
    <div class="contact-rule" style="left:163px"></div>
    <div class="contact" style="left:189px"><div class="contact__name">LIAM</div><div class="contact__phone">0431 672 095</div><div class="contact__email">lhartwell@terradiesel-example.com.au</div></div>
    <div class="contact-rule" style="left:322px"></div>
    <div class="contact" style="left:349px"><div class="contact__name">SIMON</div><div class="contact__phone">0465 218 347</div><div class="contact__email">sbrack@terradiesel-example.com.au</div></div>
  </div>
</section>

</body>
</html>
```